Business Card and Logo Color Scheme Design Contest

We are starting a new company called Lone Ridge Structural Partners and already have a logo however, the colors for the logo itself are not final and COULD be changed. I'm hoping to move AWAYfrom the gold color in the card and the logo as it seems a bit outdated. What we need help with is to find what our business color scheme will be, and then incorporate those colors into both the logo and the business card design itself. We also want to make sure we are known as "LRS" so in the future we can just refer to ourselves as "LRS" and not Lone Ridge Structural Partners. That being said, I would like to make a slight change to the logo to somehow include the letters "LRS." The logo used in the front of the card design MUST ALSO include the words "Firm No. 64307" within the logo. My vision is for the front of the card to have the information shown in the attached image. For the back of the card, I'm hoping to have something very simple. I'm envisioning a solid color with either the website (www.bridgemarkplans.com) and a simplified version of the logo. I've attached an example but I'm looking for a complete redesign. I'm looking for a slick, modern and simple design.

Industry/Entity Type

Civil Engineer

Contact Information for Business Card

Logo
Firm No. 64307
Marcus Holloway, PE
Chief Operating Officer
Email:mholloway@bridgemarkplans.com
Ph: 936.555.0142 | D: 936.555.0178 | M:210.555.0263
4187 W. Kellingham, Conroe, Texas 77301
www.bridgemarkplans.com

Requirements
Must have
• Logo
Contact Info
Nice to have
• "LRS" Incorporated in the design
Should not have
• The current color scheme

```html
<!DOCTYPE html>
<html lang="en">
<head>
<meta charset="utf-8">
<title>Lone Ridge Structural Partners — Business Card</title>
<link rel="stylesheet" href="https://fonts.googleapis.com/css2?family=Tinos:wght@400;700&display=swap">
<style>
  :root {
    --maroon: #5a1628;
    --paper: #f4f4f2;
    --ink: #333333;
    --grey: #8a8a8a;
    --rule: #9a9a9a;
    --backdrop: #d9d9d9;
    --white: #ffffff;
  }
  * { margin: 0; padding: 0; box-sizing: border-box; }
  html, body {
    width: 1200px; height: 1200px; overflow: hidden;
    background: var(--backdrop);
    font-family: "Tinos", "Times New Roman", serif;
  }
  .sheet { position: relative; width: 1200px; height: 1200px; }
  .card {
    position: absolute; left: 180px; width: 840px; height: 480px;
    box-shadow: 0 6px 18px rgba(0,0,0,0.12);
  }
  /* Back of card */
  .card-back { top: 90px; background: var(--maroon); color: var(--white); }
  .back-mark {
    position: absolute; top: 150px; left: 0; width: 100%;
    text-align: center; font-size: 110px; font-weight: 400; letter-spacing: 6px;
  }
  .back-url {
    position: absolute; top: 330px; left: 0; width: 100%;
    text-align: center; font-size: 24px; letter-spacing: 6px; text-transform: uppercase;
  }
  /* Front of card */
  .card-front { top: 630px; background: var(--paper); color: var(--ink); }
  .brand { position: absolute; top: 70px; left: 120px; width: 640px; }
  .brand-row { display: flex; align-items: center; gap: 20px; }
  .brand-square { width: 60px; height: 60px; background: var(--maroon); flex: none; }
  .brand-name { font-size: 40px; font-weight: 700; color: var(--maroon); line-height: 1; }
  .brand-rule { margin-top: 16px; margin-left: 80px; height: 2px; background: var(--rule); }
  .firm-no { margin-top: 6px; text-align: right; font-size: 16px; color: var(--grey); }
  .person { position: absolute; left: 0; top: 290px; }
  .person-tab {
    position: absolute; left: 40px; top: 4px; width: 56px; height: 56px;
    background: var(--maroon);
  }
  .person-text { position: absolute; left: 120px; top: 0; width: 380px; }
  .person-name { font-size: 28px; font-weight: 700; color: var(--ink); white-space: nowrap; }
  .person-title {
    font-size: 19px; color: var(--grey); text-transform: uppercase;
    letter-spacing: 1px; margin-top: 2px; white-space: nowrap;
  }
  .contact-line {
    display: flex; align-items: center; gap: 14px;
    font-size: 20px; color: var(--ink); margin-top: 10px; white-space: nowrap;
  }
  .contact-line svg { flex: none; fill: var(--maroon); }
  .divider {
    position: absolute; left: 540px; top: 270px; width: 2px; height: 140px;
    background: var(--rule);
  }
  .office { position: absolute; left: 580px; top: 270px; width: 240px; }
  .office-block { display: flex; align-items: flex-start; gap: 14px; margin-bottom: 20px; }
  .office-block svg { flex: none; fill: var(--maroon); margin-top: 14px; }
  .office-lines { font-size: 20px; line-height: 1.3; color: var(--ink); }
</style>
</head>
<body>
<main class="sheet">
  <section class="card card-back" aria-label="Card back">
    <div class="back-mark">LRS</div>
    <div class="back-url">www.bridgemarkplans.com</div>
  </section>

  <section class="card card-front" aria-label="Card front">
    <div class="brand">
      <div class="brand-row">
        <span class="brand-square"></span>
        <span class="brand-name">Lone Ridge Structural Partners</span>
      </div>
      <div class="brand-rule"></div>
      <div class="firm-no">Firm No. 64307</div>
    </div>

    <div class="person">
      <span class="person-tab"></span>
      <div class="person-text">
        <div class="person-name">Marcus Holloway, PE</div>
        <div class="person-title">Chief Operating Officer</div>
        <div class="contact-line">
          <svg width="16" height="24" viewBox="0 0 16 24" aria-hidden="true"><path d="M3 0h10a3 3 0 0 1 3 3v18a3 3 0 0 1-3 3H3a3 3 0 0 1-3-3V3a3 3 0 0 1 3-3zm0 3v15h10V3zm5 17a1.3 1.3 0 1 0 0 2.6A1.3 1.3 0 0 0 8 20z"/></svg>
          <span>210.555.0263</span>
        </div>
        <div class="contact-line">
          <svg width="22" height="16" viewBox="0 0 22 16" aria-hidden="true"><path d="M0 0h22v2L11 9 0 2zm0 4l11 7 11-7v12H0z"/></svg>
          <span>mholloway@bridgemarkplans.com</span>
        </div>
      </div>
    </div>

    <div class="divider"></div>

    <div class="office">
      <div class="office-block">
        <svg width="20" height="20" viewBox="0 0 20 20" aria-hidden="true"><path d="M4 1l3 0 2 5-2.5 1.5a11 11 0 0 0 6 6L14 11l5 2v3a2 2 0 0 1-2 2A16 16 0 0 1 2 3a2 2 0 0 1 2-2z"/></svg>
        <div class="office-lines">936.555.0142<br>936.555.0178</div>
      </div>
      <div class="office-block">
        <svg width="18" height="24" viewBox="0 0 18 24" aria-hidden="true"><path d="M9 0a9 9 0 0 1 9 9c0 6-9 15-9 15S0 15 0 9a9 9 0 0 1 9-9zm0 5a4 4 0 1 0 0 8 4 4 0 0 0 0-8z"/></svg>
        <div class="office-lines">4187 W. Kellingham,<br>Conroe, Texas 77301</div>
      </div>
    </div>
  </section>
</main>
</body>
</html>
```